Sales pitch for "Tidewell Crate"

We need a new sales pitch deck (and company logo) for our new company "Tidewell Crate". We collect surplus foods & goods and resell them at a discounted price to end-customers and businesses.
Show why / mission of what we do is important (combat global warming, etc.), what our concept is, who we are, why they should join / what we look for,
The story-line and content can be found in the attached Powerpoint file.
Target Market(s)
Food manufacturers, retailers, distributors, wholesale
Industry/Entity Type
Food & beverages
Requirements
Must have
- Editable PowerPoint (16:9), use storyline in attached file. You may split or combine slides, shorten / edit content, use new imagery, etc.
Nice to have
- Professional, clean, sustainable, fresh, ...
Should not have
- Funny, comics / cartoons, ...

```html
<!DOCTYPE html>
<html lang="en">
<head>
<meta charset="UTF-8">
<title>Tidewell Crate Online – Expansion</title>
<link href="https://fonts.googleapis.com/css2?family=Montserrat:wght@600;700&family=Lato:wght@300;400;700&display=swap" rel="stylesheet">
<style>
  :root {
    --sky-top: #62d4ef;
    --sky-mid: #3aa9d8;
    --sky-bottom: #0f5e98;
    --white: #ffffff;
    --navy: #0c2f5c;
    --panel-top: #2e6aa2;
    --panel-bottom: #0f3566;
    --pill-top: #6ad8f2;
    --pill-bottom: #1d6aa6;
    --pill-edge: #0a2c55;
    --store-awning: #f4c430;
    --store-body: #e8eef2;
    --store-base: #f26a3a;
  }
  * { margin: 0; padding: 0; box-sizing: border-box; }
  html, body { width: 1200px; height: 675px; overflow: hidden; }
  body { font-family: "Lato", sans-serif; color: var(--white); }

  .slide {
    position: relative;
    width: 1200px;
    height: 675px;
    overflow: hidden;
    background: linear-gradient(180deg, var(--sky-top) 0%, var(--sky-mid) 50%, var(--sky-bottom) 100%);
  }

  .slide-title {
    position: absolute;
    left: 144px; top: 24px;
    font-family: "Montserrat", sans-serif;
    font-weight: 700;
    font-size: 38px;
    letter-spacing: 1px;
    white-space: nowrap;
  }

  .column-label {
    position: absolute;
    top: 176px;
    font-family: "Montserrat", sans-serif;
    font-weight: 700;
    font-size: 20px;
  }
  .column-label::after {
    content: "";
    position: absolute;
    left: 4px; top: 35px;
    height: 2px;
    background: rgba(255,255,255,0.85);
  }
  .label-today { left: 118px; }
  .label-today::after { width: 245px; }
  .label-expansion { left: 612px; }
  .label-expansion::after { width: 217px; }

  .store-visual {
    position: absolute;
    left: 120px; top: 251px;
    width: 214px; height: 166px;
    border-radius: 6px;
    background: linear-gradient(180deg, var(--store-awning) 0%, var(--store-awning) 38%, var(--store-body) 38%, var(--store-body) 88%, var(--store-base) 88%);
  }

  .opening-hours {
    position: absolute;
    left: 227px; top: 455px;
    transform: translateX(-50%);
    font-size: 22px;
    font-weight: 700;
    white-space: nowrap;
  }

  .flow-arrow { position: absolute; left: 469px; top: 281px; }

  .webshop-panel {
    position: absolute;
    left: 612px; top: 246px;
    width: 371px; height: 246px;
    background: linear-gradient(180deg, var(--panel-top), var(--panel-bottom));
    box-shadow: 0 3px 8px rgba(0,0,0,0.35);
    border: 1px solid var(--pill-edge);
  }
  .webshop-reflection {
    position: absolute;
    left: 612px; top: 492px;
    width: 371px; height: 150px;
    background: linear-gradient(180deg, rgba(15,53,102,0.45), rgba(15,53,102,0));
  }
  .webshop-title {
    position: absolute;
    left: 0; right: 0; top: 11px;
    text-align: center;
    font-family: "Montserrat", sans-serif;
    font-weight: 700;
    font-size: 21px;
  }
  .channel {
    position: absolute;
    left: 12px; width: 349px;
    border-radius: 9px;
    border: 1px solid var(--pill-edge);
    background: linear-gradient(180deg, var(--pill-top) 0%, var(--pill-bottom) 100%);
    text-align: center;
    font-size: 18px;
    font-weight: 300;
    line-height: 1.25;
    display: flex; flex-direction: column; justify-content: center;
  }
  .channel strong { font-family: "Montserrat", sans-serif; font-weight: 700; font-size: 17px; }
  .channel-events { top: 40px; height: 38px; }
  .channel-b2c { top: 88px; height: 60px; }
  .channel-b2b { top: 158px; height: 65px; }

  .corner-lines { position: absolute; left: 900px; top: 280px; }
</style>
</head>
<body>
<main class="slide">
  <h1 class="slide-title">TIDEWELL CRATE ONLINE</h1>

  <h2 class="column-label label-today">TODAY</h2>
  <div class="store-visual" role="img" aria-label="Illustration of the shop storefront with striped awning"></div>
  <p class="opening-hours">Mo-Sa 09:00-18:30</p>

  <svg class="flow-arrow" width="32" height="156" viewBox="0 0 32 156" aria-hidden="true">
    <polygon points="0,0 30,78 0,156" fill="var(--navy)"/>
  </svg>

  <h2 class="column-label label-expansion">Expansion</h2>
  <div class="webshop-reflection"></div>
  <section class="webshop-panel">
    <h3 class="webshop-title">Web Shop</h3>
    <div class="channel channel-events"><strong>CATERINGS / EVENTS</strong></div>
    <div class="channel channel-b2c"><strong>B2C</strong><span>(incl. Subscriptions)</span></div>
    <div class="channel channel-b2b"><strong>B2B</strong><span>(restaurants, hotels, camps, etc.)</span></div>
  </section>

  <svg class="corner-lines" width="300" height="340" viewBox="0 0 300 340" aria-hidden="true">
    <g stroke="var(--white)" fill="none">
      <line x1="300" y1="10" x2="210" y2="100" stroke-width="1" opacity="0.7"/>
      <line x1="300" y1="30" x2="125" y2="205" stroke-width="3" opacity="0.9"/>
      <line x1="300" y1="48" x2="113" y2="230" stroke-width="1" opacity="0.7"/>
      <line x1="300" y1="80" x2="175" y2="210" stroke-width="3" opacity="0.9"/>
      <line x1="300" y1="125" x2="106" y2="328" stroke-width="1" opacity="0.6"/>
    </g>
  </svg>
</main>
</body>
</html>
```